Software Company Business Card Design

We are looking for a business card design for a software, messaging & IT services company based in Australia.

Talvora Group is the holding company for 3 brands all offering technology based business solutions; Talvora, Brindle & Quillpad. Brand Identity = Friendly, Professional, Viable, Vibrant, Creative

We want our business card to reflect that we are an innovative market leader. The design should be clean, professional and original.

This design will be used for all 3 brands.

More information about our company can be found at: www.talvoragroup.example.au
www.brindle.example.au

Details we would like on the card:

Firstname Lastname
Position
Level 17, 482 Ormond Rd
North Sydney
NSW 2060
Phone: +61 2 5550 1738
Fax: +61 2 5550 1794
Mobile:
Email:
www.talvoragroup.example.au

Target Market(s)

Our business cards are given to B2B and industry professionals.

Industry/Entity Type

Business

Requirements
Must have
• The Business Card must include the same colours as the logo.
Nice to have
• We would like it to me double sided.

```html
<!DOCTYPE html>
<html lang="en">
<head>
<meta charset="utf-8">
<title>Talvora Group — Business Card</title>
<link href="https://fonts.googleapis.com/css2?family=Tinos:wght@400&display=swap" rel="stylesheet">
<style>
  :root {
    --crimson: #ab0140;
    --periwinkle: #97a3df;
    --card-white: #ffffff;
    --card-edge: #e4e4e8;
    --label-ink: #111111;
    --page: #ffffff;
  }
  * { box-sizing: border-box; margin: 0; padding: 0; }
  html, body {
    width: 1200px;
    height: 664px;
    overflow: hidden;
    background: var(--page);
    font-family: "Tinos", "Times New Roman", serif;
  }
  .sheet { position: relative; width: 1200px; height: 664px; }

  .option-label {
    position: absolute;
    color: var(--label-ink);
    font-size: 15px;
  }
  .option-label--one { left: 86px; top: 60px; }
  .option-label--two { left: 75px; top: 315px; font-size: 16px; }
  .option-label--back { left: 598px; top: 148px; font-size: 22px; }

  .card {
    position: absolute;
    border-radius: 14px;
    overflow: hidden;
  }
  .card--front { background: var(--crimson); }
  .card--option-one { left: 69px; top: 88px; width: 362px; height: 195px; }
  .card--option-two { left: 71px; top: 343px; width: 386px; height: 234px; }

  .brand-name {
    position: absolute;
    color: var(--card-white);
    font-weight: 400;
    line-height: 1;
    text-align: right;
  }
  .brand-name__main { display: block; letter-spacing: 1px; }
  .brand-name__sub { display: block; }

  .card--option-one .brand-name { left: 52px; top: 72px; width: 270px; }
  .card--option-one .brand-name__main { font-size: 54px; text-align: left; }
  .card--option-one .brand-name__sub { font-size: 20px; margin-top: 0; }

  .card--option-two .brand-name { left: 18px; top: 82px; width: 264px; }
  .card--option-two .brand-name__main { font-size: 62px; text-align: left; }
  .card--option-two .brand-name__sub { font-size: 23px; }

  .card-url {
    position: absolute;
    left: 0;
    color: var(--card-white);
    font-size: 12.5px;
    letter-spacing: 2.6px;
  }
  .card--option-one .card-url { left: 68px; bottom: 15px; }
  .card--option-two .card-url { left: 29px; bottom: 13px; font-size: 13px; }

  .stripe {
    position: absolute;
    top: 0;
    width: 6px;
    height: 100%;
    background: var(--card-white);
  }
  .stripe--a { left: 305px; }
  .stripe--b { left: 335px; }
  .stripe--c { left: 362px; }

  .card--back {
    left: 590px; top: 195px; width: 549px; height: 305px;
    background: var(--card-white);
    border: 1px solid var(--card-edge);
  }
  .back-band {
    position: absolute;
    left: 0; top: 0;
    width: 112px; height: 100%;
    background: var(--crimson);
  }
  .back-band .brand-name { left: 8px; top: 227px; width: 96px; }
  .back-band .brand-name__main { font-size: 25px; text-align: left; letter-spacing: 0.5px; }
  .back-band .brand-name__sub { font-size: 10px; }

  .holder {
    position: absolute;
    right: 24px;
    top: 62px;
    text-align: right;
  }
  .holder__name { color: var(--crimson); font-size: 19px; }
  .holder__position {
    color: var(--periwinkle);
    font-size: 15px;
    letter-spacing: 5px;
    margin-top: 2px;
    margin-right: -5px;
  }

  .contact {
    position: absolute;
    right: 12px;
    top: 196px;
    text-align: right;
    font-size: 13.8px;
    line-height: 16px;
    color: var(--crimson);
  }
  .contact__key { color: var(--periwinkle); }
</style>
</head>
<body>
<main class="sheet">
  <p class="option-label option-label--one">Front Option 1</p>
  <section class="card card--front card--option-one" aria-label="Front option 1">
    <p class="brand-name"><span class="brand-name__main">talvora</span><span class="brand-name__sub">group</span></p>
    <p class="card-url">www.talvoragroup.example.au</p>
  </section>

  <p class="option-label option-label--two">Front Option 2</p>
  <section class="card card--front card--option-two" aria-label="Front option 2">
    <p class="brand-name"><span class="brand-name__main">talvora</span><span class="brand-name__sub">group</span></p>
    <span class="stripe stripe--a"></span>
    <span class="stripe stripe--b"></span>
    <span class="stripe stripe--c"></span>
    <p class="card-url">www.talvoragroup.example.au</p>
  </section>

  <p class="option-label option-label--back">Back side of the card</p>
  <section class="card card--back" aria-label="Back side">
    <div class="back-band">
      <p class="brand-name"><span class="brand-name__main">talvora</span><span class="brand-name__sub">group</span></p>
    </div>
    <div class="holder">
      <p class="holder__name">Firstname Lastname</p>
      <p class="holder__position">Position</p>
    </div>
    <div class="contact">
      <p>Level 17, 482 Ormond Rd / North Sydney / NSW 2060</p>
      <p><span class="contact__key">Ph:</span> +61 2 5550 1738 / <span class="contact__key">F:</span> +61 2 5550 1794 / <span class="contact__key">M:</span> 0400 000 000</p>
      <p><span class="contact__key">E-mail:</span> abc@talvoragroup.example.au</p>
    </div>
  </section>
</main>
</body>
</html>
```